Harborpoint Meridian Insurance Services

we are a high end insurance agency we specialize on Auto | Home | Business | Life looking for something professional and luxuries at the same time. if you guys need anything else please let me know.

Auto | Home | Business | Life must be under logo on the back with black background.

i want the back part to be black with our gold logo on it.

Target Market(s)

Auto | Home | Business | Life

Industry/Entity Type

Insurance Broker

Contact Information for Business Card

My logo is gold so a black in the back would be nice.

Font styles to use
Serif

Colors
000000

Requirements
Must have
• Big logo on the back with black background.

```html
<!DOCTYPE html>
<html lang="en">
<head>
<meta charset="UTF-8">
<title>Harborpoint Meridian Insurance Services – Business Card</title>
<link rel="stylesheet" href="https://fonts.googleapis.com/css2?family=EB+Garamond:wght@400;500;600&family=Montserrat:wght@300;400&display=swap">
<style>
  :root {
    --page-bg: #d9d4cc;
    --card-dark: #141414;
    --card-mid: #2b2b2b;
    --card-light: #3a3a3a;
    --gold: #f2cf1f;
    --gold-deep: #d8ae12;
    --silver: #b9b9b9;
    --white: #f1f1f1;
  }
  * { box-sizing: border-box; margin: 0; padding: 0; }
  html, body { width: 1018px; height: 1200px; overflow: hidden; }
  body {
    background: var(--page-bg);
    display: flex;
    flex-direction: column;
    align-items: center;
    justify-content: center;
    gap: 52px;
    font-family: "EB Garamond", Georgia, serif;
  }
  .card {
    position: relative;
    width: 900px;
    height: 514px;
    border-radius: 4px;
    overflow: hidden;
    box-shadow: 0 10px 28px rgba(0,0,0,.28);
  }
  .card-texture {
    position: absolute; inset: 0;
    background:
      linear-gradient(135deg, transparent 0 38%, rgba(255,255,255,.035) 38% 55%, transparent 55%),
      linear-gradient(60deg, rgba(0,0,0,.25) 0 30%, transparent 30% 70%, rgba(255,255,255,.03) 70%),
      radial-gradient(ellipse at 35% 25%, var(--card-light), var(--card-mid) 45%, var(--card-dark) 100%);
  }
  .wordmark {
    font-family: "EB Garamond", Georgia, serif;
    font-variant: small-caps;
    font-weight: 600;
    color: var(--gold);
    letter-spacing: .5px;
    white-space: nowrap;
    display: flex;
    align-items: center;
  }
  .wordmark-dot {
    display: inline-block;
    border-radius: 50%;
    background: var(--gold);
  }
  .tagline {
    font-family: "Montserrat", Arial, sans-serif;
    font-weight: 300;
    color: var(--silver);
    text-transform: uppercase;
    white-space: nowrap;
  }

  /* Front */
  .front-brand { position: absolute; left: 70px; top: 92px; }
  .front-brand .wordmark { font-size: 44px; gap: 16px; }
  .front-brand .wordmark-dot { width: 22px; height: 22px; }
  .front-brand .tagline { font-size: 15px; letter-spacing: 7.5px; margin: 6px 0 0 38px; }
  .person { position: absolute; left: 108px; top: 280px; }
  .person-name { color: var(--gold); font-size: 30px; font-weight: 500; }
  .person-role { color: var(--white); font-size: 21px; margin-top: 2px; }
  .address { position: absolute; left: 108px; top: 390px; color: var(--gold); font-size: 21px; line-height: 1.35; }
  .divider {
    position: absolute; left: 548px; top: 250px; width: 2px; height: 190px;
    background: linear-gradient(to bottom, transparent, var(--gold) 30%, var(--gold) 70%, transparent);
  }
  .contacts { position: absolute; left: 584px; top: 262px; list-style: none; }
  .contacts li { display: flex; align-items: center; gap: 12px; color: var(--white); font-size: 19px; height: 38px; }
  .contacts svg { width: 20px; height: 20px; flex: none; }
  .contacts .web { color: var(--gold); padding-left: 32px; }

  /* Back */
  .back-brand { position: absolute; left: 0; right: 0; top: 150px; display: flex; flex-direction: column; align-items: center; }
  .back-brand .wordmark { font-size: 62px; gap: 22px; }
  .back-brand .wordmark-dot { width: 30px; height: 30px; }
  .back-brand .tagline { font-size: 22px; letter-spacing: 11px; margin-top: 10px; }
  .services {
    margin-top: 34px;
    font-family: "EB Garamond", Georgia, serif;
    font-variant: small-caps;
    color: var(--silver);
    font-size: 22px;
    letter-spacing: 2px;
  }
  .services .sep { color: var(--gold); margin: 0 12px; }
</style>
</head>
<body>

  <section class="card card-front" aria-label="Business card front">
    <div class="card-texture" role="img" aria-label="Dark faceted polygon background texture"></div>

    <div class="front-brand">
      <div class="wordmark"><span class="wordmark-dot"></span>Harborpoint Meridian</div>
      <div class="tagline">Insurance Services</div>
    </div>

    <div class="person">
      <div class="person-name">Daniel Whitcombe</div>
      <div class="person-role">Chief Operating Officer</div>
    </div>
    <div class="address">2400 Seabright Ave<br>Port Alder, California</div>

    <div class="divider"></div>

    <ul class="contacts">
      <li>
        <svg viewBox="0 0 20 20" aria-hidden="true"><rect x="1" y="2" width="18" height="16" rx="2" fill="var(--gold)"/><path d="M6 6c0 5 3 8 8 8l1-2-2-1-1 1c-2-1-3-2-4-4l1-1-1-2z" fill="var(--card-dark)"/></svg>
        +1555-204-7318
      </li>
      <li>
        <svg viewBox="0 0 20 20" aria-hidden="true"><rect x="1" y="2" width="18" height="16" rx="2" fill="var(--gold)"/><rect x="7" y="5" width="6" height="10" rx="1" fill="var(--card-dark)"/></svg>
        +1555-309-6642
      </li>
      <li>
        <svg viewBox="0 0 20 20" aria-hidden="true"><rect x="1" y="2" width="18" height="16" rx="2" fill="var(--gold)"/><path d="M4 6h12v8H4z" fill="var(--card-dark)"/><path d="M4 6l6 5 6-5" stroke="var(--gold)" stroke-width="1.2" fill="none"/></svg>
        daniel@harborpointmeridian.com
      </li>
      <li class="web">www.harborpointmeridian.com</li>
    </ul>
  </section>

  <section class="card card-back" aria-label="Business card back">
    <div class="card-texture" role="img" aria-label="Dark faceted polygon background texture"></div>

    <div class="back-brand">
      <div class="wordmark"><span class="wordmark-dot"></span>Harborpoint Meridian</div>
      <div class="tagline">Insurance Services</div>
      <div class="services">Auto<span class="sep">|</span>Home<span class="sep">|</span>Business<span class="sep">|</span>Life</div>
    </div>
  </section>

</body>
</html>
```